Book Cover Design

Design with title UNWAVERING
Subtitle: Ways to Kindle the Spark of Resolve
Author Name: Carla Jean Morrow
Put DAILY MERIDIAN BESTSELLER at top
Shimmer design, see inspirational images attached

```html
<!DOCTYPE html>
<html lang="en">
<head>
<meta charset="utf-8">
<title>Unwavering — Book Cover</title>
<link rel="stylesheet" href="https://fonts.googleapis.com/css2?family=Oswald:wght@500&family=Jost:wght@400;500;600&display=swap">
<style>
  :root {
    --stage-bg: #dcdcdc;
    --cover-light: #e8e7e5;
    --cover-mid: #dedcd8;
    --cover-warm: #e6d5bc;
    --cover-edge: #f4f4f2;
    --gold-dark: #a06d2a;
    --gold-light: #c99a50;
    --ink: #474747;
  }
  * { margin: 0; padding: 0; box-sizing: border-box; }
  html, body {
    width: 1200px;
    height: 900px;
    overflow: hidden;
    background: var(--stage-bg);
  }
  .stage {
    position: relative;
    width: 1200px;
    height: 900px;
  }
  .book-cover {
    position: absolute;
    left: 353px;
    top: 99px;
    width: 493px;
    height: 702px;
    border: 1px solid var(--cover-edge);
    background:
      radial-gradient(ellipse at 20% 30%, rgba(255,255,255,0.35), transparent 55%),
      radial-gradient(ellipse at 80% 60%, rgba(190,190,186,0.25), transparent 60%),
      linear-gradient(180deg, var(--cover-light) 0%, var(--cover-mid) 55%, #dfd9cf 78%, var(--cover-warm) 100%);
  }
  .cover-title {
    position: absolute;
    top: 104px;
    left: 0;
    width: 100%;
    text-align: center;
    font-family: "Oswald", sans-serif;
    font-weight: 500;
    font-size: 82px;
    line-height: 1;
    letter-spacing: 6px;
    padding-left: 6px;
    background: linear-gradient(90deg, var(--gold-dark) 0%, var(--gold-light) 50%, var(--gold-dark) 100%);
    -webkit-background-clip: text;
    background-clip: text;
    color: transparent;
    transform: scaleY(1.12);
    transform-origin: top center;
  }
  .cover-subtitle {
    position: absolute;
    top: 238px;
    left: 0;
    width: 100%;
    text-align: center;
    font-family: "Jost", sans-serif;
    font-weight: 600;
    font-size: 21px;
    color: var(--ink);
  }
  .cover-note {
    position: absolute;
    top: 540px;
    left: 49px;
    font-family: "Jost", sans-serif;
    font-weight: 400;
    font-size: 22px;
    line-height: 31px;
    color: var(--ink);
  }
  .cover-author {
    position: absolute;
    top: 637px;
    left: 0;
    width: 100%;
    text-align: center;
    font-family: "Jost", sans-serif;
    font-weight: 600;
    font-size: 25px;
    letter-spacing: 0.2em;
    color: var(--gold-dark);
  }
</style>
</head>
<body>
  <div class="stage">
    <div class="book-cover">
      <h1 class="cover-title">UNWAVERING</h1>
      <p class="cover-subtitle">Ways to Kindle the Spark of Resolve</p>
      <p class="cover-note">Put DAILY MERIDIAN BESTSELLER<br>at top Shimmer design</p>
      <p class="cover-author">Carla Jean Morrow</p>
    </div>
  </div>
</body>
</html>
```